Beauty Salon Design

The business card design will be for a new beauty salon opening up.

The therapist has over 11 years at a leading beauty Salon in perth.

The two colours that the salon will use is black and gold.

Industry/Entity Type

Beauty Salon

Contact Information for Business Card

Lumora Beauty

Corinne Halstead Pryce
Advanced beauty therapist
0455 817 302

Monday - Friday 9am - 2.30pm
Weekends and nights by appointment only

Waxing, Tinting, Swedish massage, hot stone massage, facials, peels, micro, LED light treatment, skin needling and retail products.

```html
<!DOCTYPE html>
<html lang="en">
<head>
<meta charset="utf-8">
<title>Lumora Beauty – Business Card</title>
<link rel="stylesheet" href="https://fonts.googleapis.com/css2?family=Quicksand:wght@400;500&display=swap">
<style>
  :root {
    --backdrop: #4d5758;
    --card: #141718;
    --card-edge: #1c2021;
    --gold: #d8c619;
    --gold-soft: #a69a1e;
    --gold-dim: #7d7522;
    --grey-text: #6d7373;
    --figure-dark: #0b0d0e;
  }
  * { margin: 0; padding: 0; box-sizing: border-box; }
  html, body {
    width: 1200px; height: 741px; overflow: hidden;
    background: var(--backdrop);
    font-family: "Quicksand", sans-serif;
  }
  .canvas { position: relative; width: 1200px; height: 741px; }

  .card {
    position: absolute; left: 399px; width: 410px; height: 238px;
    background: linear-gradient(180deg, var(--card-edge), var(--card));
    overflow: hidden;
  }
  .card--front { top: 89px; }
  .card--back { top: 413px; }

  .stripes { position: absolute; display: block; }
  .stripes line { stroke: var(--gold); stroke-width: 1.4; }

  /* front */
  .figure-art {
    position: absolute; left: 118px; top: 0; width: 228px; height: 238px;
    background: radial-gradient(ellipse at 55% 45%, var(--figure-dark) 0%, rgba(11,13,14,0.7) 45%, rgba(20,23,24,0) 75%);
  }
  .stripes--front-left { left: 0; top: 55px; }
  .stripes--front-right { left: 289px; top: 55px; }
  .brand-name {
    position: absolute; left: 34px; top: 54px; width: 250px;
    font-size: 27px; font-weight: 400; color: var(--gold);
    letter-spacing: 0.5px; white-space: nowrap; line-height: 34px; text-align: center;
  }
  .opening-hours {
    position: absolute; right: 5px; bottom: 5px;
    font-size: 10.5px; color: var(--gold-soft); white-space: nowrap;
  }

  /* back */
  .stripes--back-left { left: 0; top: 49px; }
  .stripes--back-right { left: 400px; top: 49px; }
  .therapist { position: absolute; left: 191px; top: 46px; white-space: nowrap; }
  .therapist__name { font-size: 18px; font-weight: 400; color: var(--gold); line-height: 22px; }
  .therapist__role { font-size: 14.5px; color: var(--gold-soft); line-height: 18px; letter-spacing: 0.3px; }

  .services {
    position: absolute; left: 21px; top: 124px; list-style: none;
    font-size: 11.5px; color: var(--gold-dim); line-height: 18.5px;
  }
  .services li { white-space: nowrap; word-spacing: 2px; }

  .appointments {
    position: absolute; left: 4px; bottom: 5px;
    font-size: 10.5px; color: var(--grey-text); white-space: nowrap;
  }
  .contact-phone {
    position: absolute; right: 4px; bottom: 4px;
    display: flex; align-items: center; gap: 6px;
    font-size: 11px; color: var(--gold-soft); letter-spacing: 2px; white-space: nowrap;
  }
  .contact-phone svg { display: block; }
</style>
</head>
<body>
<main class="canvas">

  <section class="card card--front">
    <div class="figure-art" role="img" aria-label="Faint illustration of a woman's silhouette with long wavy hair"></div>

    <svg class="stripes stripes--front-left" width="23" height="34" viewBox="0 0 23 34" aria-hidden="true">
      <line x1="0" y1="2" x2="23" y2="2"/><line x1="0" y1="9" x2="23" y2="9"/>
      <line x1="0" y1="16" x2="23" y2="16"/><line x1="0" y1="24" x2="23" y2="24"/>
      <line x1="0" y1="31" x2="23" y2="31"/>
    </svg>
    <h1 class="brand-name">Lumora Beauty</h1>
    <svg class="stripes stripes--front-right" width="121" height="34" viewBox="0 0 121 34" aria-hidden="true">
      <line x1="0" y1="2" x2="121" y2="2"/><line x1="0" y1="9" x2="121" y2="9"/>
      <line x1="0" y1="16" x2="121" y2="16"/><line x1="0" y1="24" x2="121" y2="24"/>
      <line x1="0" y1="31" x2="121" y2="31"/>
    </svg>

    <p class="opening-hours">Monday - Friday 9am - 2.30pm</p>
  </section>

  <section class="card card--back">
    <svg class="stripes stripes--back-left" width="183" height="34" viewBox="0 0 183 34" aria-hidden="true">
      <line x1="0" y1="2" x2="183" y2="2"/><line x1="0" y1="9" x2="183" y2="9"/>
      <line x1="0" y1="16" x2="183" y2="16"/><line x1="0" y1="24" x2="183" y2="24"/>
      <line x1="0" y1="31" x2="183" y2="31"/>
    </svg>
    <div class="therapist">
      <h2 class="therapist__name">Corinne Halstead Pryce</h2>
      <p class="therapist__role">Advanced beauty therapist</p>
    </div>
    <svg class="stripes stripes--back-right" width="10" height="34" viewBox="0 0 10 34" aria-hidden="true">
      <line x1="0" y1="2" x2="10" y2="2"/><line x1="0" y1="9" x2="10" y2="9"/>
      <line x1="0" y1="16" x2="10" y2="16"/><line x1="0" y1="24" x2="10" y2="24"/>
      <line x1="0" y1="31" x2="10" y2="31"/>
    </svg>

    <ul class="services">
      <li>hot stone massage</li>
      <li>skin needling &nbsp; swedish massage</li>
      <li>retail products &nbsp;waxing &nbsp;tinting</li>
      <li>facials, peels, micro LED light treatment</li>
    </ul>

    <p class="appointments">Weekends and nights by appointment only</p>
    <p class="contact-phone">
      <svg width="8" height="13" viewBox="0 0 8 13" aria-hidden="true">
        <rect x="0.6" y="0.6" width="6.8" height="11.8" rx="1" fill="none" stroke="var(--gold-soft)" stroke-width="1.2"/>
        <rect x="2" y="2.2" width="4" height="5.5" fill="var(--gold-soft)"/>
        <circle cx="4" cy="10.2" r="0.9" fill="var(--gold-soft)"/>
      </svg>
      <span>0455 817 302</span>
    </p>
  </section>

</main>
</body>
</html>
```